New business card for UK roofing company

We are Brindmore Roofing and we need a business card design for our staff.

We offer the following services:

- New roofs
- General roof repairs
- Drone surveys
- Single ply roofing
- Steel cladding
- Asbestos removal
- Electronic leak detection

I have attached our logo. I have also attached example branding printed to our vans. The business card should fit in with the style of our branding.

The business card should have the following information;

Address:
Unit 17c Wendlecroft Farm
Wendlecroft Lane
Hatchington
CM4 9QD

Telephone: 020 7946 0372
24 Hour: 0800 612 4479

Email: ray@brindmoreroofing.example
Mobile: 07700981234
Name: Ray Tunstead
Website: www.brindmoreroofing.example

The business card will be printed in Spot UV, see here: https://www.kestaprint.example/business-cards/spot-uv/

If you need anymore info, please let me know,

```html
<!DOCTYPE html>
<html lang="en">
<head>
<meta charset="utf-8">
<title>Brindmore Roofing – Business Card</title>
<link rel="stylesheet" href="https://fonts.googleapis.com/css2?family=Montserrat:wght@500;600;700;800&display=swap">
<style>
  :root {
    --bg: #3a3a3c;
    --navy: #12467a;
    --navy-dark: #0f3a66;
    --silver: #c9cbce;
    --cyan: #29a9e0;
    --ink: #3b3f45;
    --white: #ffffff;
    --faint: #e6f4fa;
    --faint-ring: #eceff3;
  }
  * { box-sizing: border-box; margin: 0; padding: 0; }
  html, body { width: 1200px; height: 689px; overflow: hidden; }
  body {
    background: var(--bg);
    font-family: "Montserrat", Arial, sans-serif;
    position: relative;
  }
  .card {
    position: absolute;
    top: 176px;
    width: 520px;
    height: 336px;
    border-radius: 22px;
    overflow: hidden;
  }
  /* Front */
  .card-front {
    left: 50px;
    background: var(--navy);
    color: var(--white);
  }
  .front-brand {
    position: absolute;
    top: 104px;
    left: 0; right: 0;
    text-align: center;
    display: flex;
    align-items: center;
    justify-content: center;
    gap: 14px;
  }
  .front-brand .brand-dot {
    width: 46px; height: 46px;
    border-radius: 50%;
    background: var(--silver);
  }
  .front-brand .brand-name {
    font-weight: 800;
    font-size: 44px;
    letter-spacing: -1.5px;
    color: var(--silver);
  }
  .services {
    position: absolute;
    left: 0; right: 0;
    bottom: 54px;
    text-align: center;
    font-weight: 500;
    font-size: 14px;
    line-height: 22px;
  }
  .services .sep {
    display: inline-block;
    width: 6px; height: 6px;
    border-radius: 50%;
    background: var(--cyan);
    margin: 0 6px;
    vertical-align: middle;
  }
  /* Back */
  .card-back {
    left: 630px;
    background: var(--white);
    color: var(--ink);
  }
  .back-decor {
    position: absolute;
    left: 70px; top: 40px;
  }
  .person {
    position: absolute;
    left: 36px; top: 36px;
  }
  .person-name {
    font-weight: 800;
    font-size: 26px;
    color: var(--navy-dark);
    letter-spacing: 0.5px;
  }
  .person-email {
    font-size: 13px;
    font-weight: 500;
    color: var(--cyan);
    margin-top: 2px;
  }
  .back-brand {
    position: absolute;
    right: 30px; top: 40px;
    display: flex;
    align-items: center;
    gap: 8px;
  }
  .back-brand .brand-dot {
    width: 22px; height: 22px;
    border-radius: 50%;
    background: var(--cyan);
  }
  .back-brand .brand-name {
    font-weight: 800;
    font-size: 20px;
    letter-spacing: -0.6px;
    color: var(--cyan);
  }
  .contact {
    position: absolute;
    left: 36px; top: 140px;
    list-style: none;
    font-size: 14px;
    font-weight: 500;
    line-height: 21px;
  }
  .contact li {
    display: flex;
    align-items: flex-start;
    gap: 12px;
    margin-bottom: 6px;
  }
  .contact svg { flex: none; margin-top: 3px; }
  .contact .strong { font-weight: 700; }
</style>
</head>
<body>

<section class="card card-front" aria-label="Business card front">
  <div class="front-brand">
    <span class="brand-dot"></span>
    <span class="brand-name">brindmoreroofing</span>
  </div>
  <p class="services">
    New Roofs<span class="sep"></span>General Roof Repairs<span class="sep"></span>Drone Surveys<span class="sep"></span>Single Ply Roofing<br>
    Steel Cladding<span class="sep"></span>Asbestos Removal<span class="sep"></span>Electronic Leak Detection
  </p>
</section>

<section class="card card-back" aria-label="Business card back">
  <svg class="back-decor" width="260" height="260" viewBox="0 0 260 260" aria-hidden="true">
    <circle cx="130" cy="130" r="126" fill="var(--faint)" stroke="var(--faint-ring)" stroke-width="6"/>
  </svg>

  <div class="person">
    <h1 class="person-name">RAY TUNSTEAD</h1>
    <p class="person-email">ray@brindmoreroofing.example</p>
  </div>

  <div class="back-brand">
    <span class="brand-dot"></span>
    <span class="brand-name">brindmoreroofing</span>
  </div>

  <ul class="contact">
    <li>
      <svg width="12" height="16" viewBox="0 0 12 16"><path d="M6 0a6 6 0 0 0-6 6c0 4.5 6 10 6 10s6-5.5 6-10a6 6 0 0 0-6-6zm0 8.5A2.5 2.5 0 1 1 6 3.5a2.5 2.5 0 0 1 0 5z" fill="var(--cyan)"/></svg>
      <span>Unit 17c Wendlecroft Farm<br>Wendlecroft Lane<br>Hatchington, CM4 9QD</span>
    </li>
    <li>
      <svg width="14" height="14" viewBox="0 0 24 24"><path d="M6.6 10.8a15 15 0 0 0 6.6 6.6l2.2-2.2a1 1 0 0 1 1-.25 11.4 11.4 0 0 0 3.6.57 1 1 0 0 1 1 1V20a1 1 0 0 1-1 1A17 17 0 0 1 3 4a1 1 0 0 1 1-1h3.5a1 1 0 0 1 1 1c0 1.25.2 2.45.57 3.57a1 1 0 0 1-.25 1z" fill="var(--cyan)"/></svg>
      <span class="strong">020 7946 0372<br>0800 612 4479 (24Hr)</span>
    </li>
    <li>
      <svg width="12" height="16" viewBox="0 0 12 16"><rect x="1" y="0.8" width="10" height="14.4" rx="2" fill="none" stroke="var(--cyan)" stroke-width="1.6"/><circle cx="6" cy="12.4" r="1" fill="var(--cyan)"/></svg>
      <span>0770 098 1234</span>
    </li>
    <li>
      <svg width="14" height="14" viewBox="0 0 14 14"><circle cx="7" cy="7" r="6" fill="none" stroke="var(--cyan)" stroke-width="1.6"/><path d="M1 7h12M7 1c2 2 2 10 0 12M7 1c-2 2-2 10 0 12" fill="none" stroke="var(--cyan)" stroke-width="1.2"/></svg>
      <span>brindmoreroofing.example</span>
    </li>
  </ul>
</section>

</body>
</html>
```